Taking action and overcoming fear with changes in your life. Encouraging people to make a change ...

I need a logo and basic website done in wordpress for my website boldstepnow.example. I would like an image or images showing action and overcoming fear. This is an encouragement site to motivate and inspire. Images showing challenges and overcoming challenges. Bright and exciting. Please use your own creativity.

Font styles to use
Sans Serif

Colors

Designer to choose colors to be used in the design.

```html
<!DOCTYPE html>
<html lang="en">
<head>
<meta charset="utf-8">
<title>Bold Step Now</title>
<link rel="stylesheet" href="https://fonts.googleapis.com/css2?family=Montserrat:wght@300;400;500;600;700&display=swap">
<style>
:root{
  --navy:#1e2739;
  --red:#ec2227;
  --card:#efedee;
  --logo-bg:#e0dfe0;
  --footer:#e4e3e5;
  --text:#222;
  --muted:#6a6a70;
  --row:#f8f8f8;
}
*{margin:0;padding:0;box-sizing:border-box}
html,body{width:1200px;height:2521px;overflow:hidden}
body{position:relative;background:var(--navy);font-family:"Montserrat",sans-serif;color:var(--text)}
.abs{position:absolute}
.topbar{left:0;top:0;width:1200px;height:34px;background:var(--navy)}
.topbar .tagline{left:163px;top:9px;font-size:12px;color:#fff;white-space:nowrap}
.topbar .tagline span{color:var(--red)}
.social{display:flex;gap:30px}
.social i{display:block;width:9px;height:9px;border-radius:50%;background:#fff}
.topbar .social{left:913px;top:12px}
.hero{left:0;top:34px;width:1200px;height:344px;background:linear-gradient(180deg,#c9b3c3 0%,#a89bbb 40%,#7d78a3 75%,#5f5e8b 100%)}
.footer{left:0;top:2134px;width:1200px;height:387px;background:var(--footer)}
.card{left:159px;top:77px;width:514px;height:2100px;background:var(--card)}
.logo-box{left:177px;top:96px;width:477px;height:188px;background:var(--logo-bg);display:flex;align-items:center;justify-content:center}
.brand{font-weight:700;color:var(--red);font-size:38px;letter-spacing:-.5px}
.nav{left:195px;top:306px;display:flex;gap:0}
.nav a{width:89px;text-align:center;color:var(--red);font-size:13px;text-decoration:none;display:flex;flex-direction:column;align-items:center;gap:10px}
.nav svg{width:40px;height:40px;fill:none;stroke:#222;stroke-width:1.4}
.byline{left:159px;width:514px;top:423px;text-align:center;font-size:11.5px;word-spacing:2px}
.byline b{font-weight:500;margin:0 12px}
.title{left:159px;width:514px;top:440px;text-align:center;color:var(--red);font-weight:600;font-size:52px}
.lede{left:225px;width:382px;top:518px;text-align:center;font-size:12.5px;line-height:21px;font-weight:400}
.photo{left:219px;top:606px;width:400px;height:223px;background:linear-gradient(135deg,#3a4a3f,#2b3d4b 50%,#8aa0b4)}
.meta{font-size:12.5px;color:var(--muted);font-weight:300;display:flex;align-items:center;white-space:nowrap}
.meta .sep{width:1px;height:12px;background:#ccc;margin:0 18px}
.meta svg{width:20px;height:16px;fill:none;stroke:#777;stroke-width:1.2;margin-right:8px}
.post-h{color:var(--red);font-weight:500;font-size:30px}
.body-txt{font-size:12.8px;line-height:20.7px;color:var(--muted);font-weight:300;width:396px}
.more{font-size:12.5px;color:var(--red)}
.post-social{display:flex;gap:34px}
.post-social i{display:block;width:8px;height:8px;border-radius:50%;background:#777}
.divider{left:221px;width:388px;height:1px;background:#d3d1d2}
.big-h{left:219px;top:1570px;color:var(--red);font-weight:600;font-size:44px}
.sub-h{left:219px;top:1636px;font-size:21px;font-weight:300}
.sched{left:217px;top:1697px;width:401px}
.sched li{list-style:none;height:63.6px;display:flex;padding:12px 12px 0;font-size:12.5px;line-height:20.7px;color:var(--muted);font-weight:300}
.sched li:nth-child(odd){background:var(--row)}
.sched b{color:var(--red);font-weight:500;width:44px;flex:none}
.label{background:var(--red);color:#fff;font-weight:600;padding:0 4px;line-height:25px}
.side-txt{left:756px;width:250px;color:#fff;font-size:11.5px;line-height:20.7px;font-weight:500}
.ig{width:100px;height:97px}
.f-logo{left:140px;top:2252px;font-size:18px}
.f-h{font-size:19px;font-weight:500;color:#222}
.pages{left:446px;top:2282px;width:280px;display:flex;flex-wrap:wrap;gap:3px 4px}
.pages span{border:1px solid #c6c5c8;padding:0 16px;line-height:34px;font-size:11.5px;color:#555}
.addr{left:835px;top:2282px;font-size:11.5px;line-height:20.7px;color:#555}
.f-line{left:15px;top:2437px;width:1178px;height:1px;background:#cfcdd0}
.copy{left:151px;top:2470px;font-size:11.5px;color:#555}
.f-social{left:940px;top:2466px;display:flex;gap:12px}
.f-social i{display:block;width:25px;height:25px;border:1.5px solid #666;border-radius:50%}
</style>
</head>
<body>
<header class="abs topbar">
  <p class="abs tagline"><span>Overcoming fear</span> Overcoming challenges</p>
  <div class="abs social"><i></i><i></i><i></i><i></i></div>
</header>
<div class="abs hero" role="img" aria-label="Misty purple mountain range at dusk"></div>
<footer class="abs footer"></footer>

<main class="abs card"></main>
<div class="abs logo-box"><span class="brand">boldstepnow.example</span></div>

<nav class="abs nav">
  <a href="#"><svg viewBox="0 0 40 40"><circle cx="20" cy="20" r="18"/><circle cx="20" cy="16" r="6"/><path d="M9 32c3-7 19-7 22 0"/></svg>About Me</a>
  <a href="#"><svg viewBox="0 0 40 40"><rect x="3" y="5" width="34" height="30"/><path d="M3 11h34M10 17h22M10 23h22M10 29h22"/><circle cx="7" cy="17" r="1"/><circle cx="7" cy="23" r="1"/><circle cx="7" cy="29" r="1"/></svg>Blog</a>
  <a href="#"><svg viewBox="0 0 40 40"><rect x="14" y="3" width="12" height="22" rx="6"/><path d="M10 19c0 12 20 12 20 0M20 31v6M14 37h12"/></svg>Podcast</a>
  <a href="#"><svg viewBox="0 0 40 40"><rect x="5" y="16" width="30" height="20"/><path d="M5 16l28-8 2 6-28 8M17 22v10l8-5z"/></svg>Video</a>
  <a href="#"><svg viewBox="0 0 40 40"><path d="M4 24L34 4 26 36 18 26zM18 26l16-22M4 24l-1 10 9-6"/></svg>Contact</a>
</nav>

<p class="abs byline">By Daniel Reyes <b></b> On May 17, 2018</p>
<h1 class="abs title">Taking Action</h1>
<p class="abs lede">Vivamus molestie dictum ligula ut tincidunt. Praesent nec accumsan mi. Vivamus sollicitudin, lacus vitae mattis vulputate, nisl leo suscipit nibh.</p>
<div class="abs photo" role="img" aria-label="Smiling man in sunglasses outdoors"></div>

<article>
  <div class="abs meta" style="left:219px;top:855px">JOURNAL<span class="sep"></span>13 NOV 2012<span class="sep"></span><svg viewBox="0 0 20 16"><rect x="1" y="4" width="14" height="9"/><path d="M5 1h14v9"/></svg>8</div>
  <h2 class="abs post-h" style="left:216px;top:889px">MOTIVATE AND INSPIRE</h2>
  <div class="abs body-txt" style="left:216px;top:963px">
    <p>Praesent nec accumsan mi. Vivamus sollicitudin, lacus vitae mattis vulputate, nisl leo suscipit nibh, bibendum pellentesque felis tellus eu sapien. Morbi ac diam at leo dapibus pretium. Aenean blandit viverra vulputate. Nam fringilla odio eu erat rhoncus, eget mollis justo finibus.</p>
    <p style="margin-top:20.7px">Suspendisse eu nulla tortor. Praesent nec accumsan mi. Vivamus sollicitudin, lacus vitae mattis vulputate, nisl leo suscipit nibh, bibendum pellentesque felis tellus eu sapien. Morbi ac diam at leo dapibus pretium.</p>
  </div>
  <a class="abs more" style="left:215px;top:1199px">CONTINUE READING</a>
  <div class="abs post-social" style="left:480px;top:1203px"><i></i><i></i><i></i><i></i></div>
</article>
<div class="abs divider" style="top:1256px"></div>

<article>
  <div class="abs meta" style="left:217px;top:1307px">JOURNAL<span class="sep"></span>13 NOV 2012<span class="sep"></span><svg viewBox="0 0 20 16"><rect x="1" y="4" width="14" height="9"/><path d="M5 1h14v9"/></svg>8</div>
  <h2 class="abs post-h" style="left:216px;top:1338px">ENCOURAGING</h2>
  <p class="abs body-txt" style="left:216px;top:1389px">Praesent nec accumsan mi. Vivamus sollicitudin, lacus vitae mattis vulputate, nisl leo suscipit nibh, bibendum pellentesque felis tellus eu sapien. Morbi ac diam.</p>
  <a class="abs more" style="left:217px;top:1478px">CONTINUE READING</a>
  <div class="abs post-social" style="left:475px;top:1482px"><i></i><i></i><i></i><i></i></div>
</article>
<div class="abs divider" style="top:1535px"></div>

<h2 class="abs big-h">Overcoming fear</h2>
<p class="abs sub-h">Overcoming challenges</p>
<ul class="abs sched">
  <li><b>23:05</b>Praesent nec accumsan mi. Vivamus sollicitudin, lacus vitae mattis vulputate, nisl leo</li>
  <li><b>23:05</b>Praesent nec accumsan mi. Vivamus sollicitudin, lacus vitae mattis vulputate, nisl leo</li>
  <li><b>23:05</b>Praesent nec accumsan mi. Vivamus sollicitudin, lacus vitae mattis vulputate, nisl leo</li>
  <li><b>23:05</b>Praesent nec accumsan mi. Vivamus sollicitudin, lacus vitae mattis vulputate, nisl leo</li>
  <li><b>23:05</b>Praesent nec accumsan mi. Vivamus sollicitudin, lacus vitae mattis vulputate, nisl leo</li>
</ul>

<aside>
  <h3 class="abs label" style="left:756px;top:483px;font-size:19px">Realistic and Attainable</h3>
  <p class="abs side-txt" style="top:528px">But I must explain to you how all this mistaken idea of denouncing pleasure and praising pain was born.</p>
  <p class="abs side-txt" style="top:610px">&nbsp;and I will give you a complete account of the system</p>
  <h3 class="abs label" style="left:756px;top:722px;font-size:18px;padding:0 8px">Instagram</h3>
  <div class="abs ig" style="left:756px;top:761px;background:linear-gradient(#e8e4e0,#b98a6c)" role="img" aria-label="Athlete standing outdoors"></div>
  <div class="abs ig" style="left:868px;top:761px;background:linear-gradient(#2aa9e0,#1a6fa0)" role="img" aria-label="Beach hut on a pier at sunset"></div>
  <div class="abs ig" style="left:756px;top:871px;background:linear-gradient(#d8d4cf,#8a7a6c)" role="img" aria-label="Woman in a wide hat laughing"></div>
  <div class="abs ig" style="left:868px;top:871px;background:linear-gradient(#9ab4cc,#b8a88e)" role="img" aria-label="Runner on a mountain road"></div>
  <div class="abs ig" style="left:756px;top:983px;background:linear-gradient(#e2dcd6,#a8a6a8)" role="img" aria-label="Woman holding a camera by the sea"></div>
  <div class="abs ig" style="left:868px;top:983px;background:linear-gradient(#4ab3c9,#0d1a20)" role="img" aria-label="Silhouettes doing yoga at sunset"></div>
</aside>

<div class="abs f-logo brand">Bold Step Now</div>
<h4 class="abs f-h" style="left:446px;top:2232px">Pages</h4>
<div class="abs pages"><span>ABOUT ME</span><span>BLOG</span><span>PODCAST</span><span>VIDEO</span><span>CONTACT</span></div>
<h4 class="abs f-h" style="left:835px;top:2232px">Address</h4>
<p class="abs addr">Bold Step Now<br>48 Harbor Lane, Millbrook, TX 70010<br><br>Phone: 555.010.2040<br>E-mail: hello@boldstepnow.example</p>
<div class="abs f-line"></div>
<p class="abs copy">COPYRIGHT © 2019 Bold Step Now</p>
<div class="abs f-social"><i></i><i></i><i></i></div>
</body>
</html>
```